Beekeeping company in need of a new attractive, simple website

We need a simple website for our Company 'Ridgecrest Apiary LLC' that will feature a couple different products that we offer (2019 NUCS & 2019 Queens) with the ability for customers to place orders for those products. Products will be for pickup only on specific dates so no shipping is required but will need dropdown menus to select which dates with limited quantities each date. Payments can be made through Coinvane, Plimo, and Tallyo. Need the to ability to add and remove products from view on the site while maintaining information. Would like the ability to build a mailing list of potential customers and also connect visitors to our social media sites.
Target Market(s)
Beekeepers,
Colors
Designer to choose colors to be used in the design.
Look and feel

```html
<!DOCTYPE html>
<html lang="en">
<head>
<meta charset="utf-8">
<title>Ridgecrest Apiary LLC</title>
<link rel="stylesheet" href="https://fonts.googleapis.com/css2?family=Cinzel:wght@400;700&family=Playfair+Display:ital@1&family=Raleway:ital,wght@0,400;0,500;0,600;0,700;1,400&family=Signika:wght@500;600;700&display=swap">
<style>
:root{
  --cream:#fde9b2;
  --yellow:#fdd835;
  --yellow-deep:#f9c520;
  --amber:#c8780a;
  --amber-dark:#a35f06;
  --orange:#ef6d2e;
  --brown:#3b2106;
  --brown-band:#8a5a0b;
  --ink:#2b1a08;
  --muted:#6b5a40;
  --paper:#f7f5ef;
  --white:#ffffff;
  --star:#f3b51e;
}
*{margin:0;padding:0;box-sizing:border-box}
html,body{width:1200px;height:2622px;overflow:hidden}
body{position:relative;font-family:"Raleway",sans-serif;font-variant-numeric:lining-nums;color:var(--ink);background:var(--white)}
.abs{position:absolute}
.center{text-align:center}

/* top bar */
.topbar{left:0;top:0;width:1200px;height:38px;background:var(--cream);font-size:11px;color:var(--brown)}
.topbar .contact{left:238px;top:12px;display:flex;gap:22px;align-items:center}
.topbar .contact span{display:flex;align-items:center;gap:7px}
.topbar .tools{left:858px;top:9px;display:flex;gap:20px;align-items:center}
.cart-count{position:absolute;left:14px;top:-4px;width:13px;height:13px;border-radius:50%;background:var(--star);font-size:8px;color:#fff;text-align:center;line-height:13px}

/* hero */
.hero{left:0;top:38px;width:1200px;height:522px;background:
  radial-gradient(ellipse 260px 180px at 700px 320px,#8a5a2a 0%,transparent 70%),
  radial-gradient(ellipse 300px 200px at 980px 180px,#e9dccb 0%,transparent 70%),
  linear-gradient(100deg,#6f6964 0%,#9a8d80 18%,#5a3b22 40%,#7a5331 60%,#4a2d15 80%,#b49a80 100%)}
.navband{left:0;top:38px;width:1200px;height:98px;background:rgba(30,20,10,.78)}
.brand{left:238px;top:62px;width:130px;text-align:center;color:var(--star);font-family:"Signika",sans-serif;font-weight:600;font-size:20px;line-height:1.1;letter-spacing:.5px}
.brand .sq{display:block;width:14px;height:14px;margin:0 auto 6px;border:2px solid var(--star);border-radius:50%}
.nav{left:633px;top:88px;display:flex;gap:16px;font-size:12px;color:#fff;font-weight:500}
.nav .sep{opacity:.8}
.badge{left:222px;top:172px;width:312px;height:356px}
.badge .text{position:absolute;left:0;top:92px;width:312px;text-align:center}
.badge .kicker{font-family:"Playfair Display",serif;font-style:italic;color:var(--star);font-size:19px}
.badge h1{font-family:"Cinzel",serif;font-weight:400;color:#fff;font-size:35px;line-height:1.22;margin-top:6px;letter-spacing:1px}
.badge .shop{display:inline-block;margin-top:18px;width:146px;height:30px;border:1.5px solid #fff;color:#fff;font-size:10px;letter-spacing:1px;line-height:27px}

/* section heads */
.eyebrow{font-size:11px;color:var(--orange);font-weight:500}
.sec-title{font-family:"Signika",sans-serif;font-weight:600;font-size:29px;color:var(--brown);line-height:1.1}
.squiggle{display:block;margin:4px auto 0}

/* services */
.services{left:0;top:560px;width:1200px;height:533px;background:var(--yellow)}
.svc-head{left:0;top:26px;width:1200px}
.svc-intro{left:405px;top:91px;width:390px;font-size:9.5px;line-height:1.6;color:var(--muted)}
.svc-item{width:200px;text-align:center}
.svc-item h3{font-family:"Signika",sans-serif;font-weight:600;font-size:17px;color:var(--brown);margin-top:14px}
.svc-item p{font-size:9.5px;line-height:1.55;color:var(--muted);margin:6px auto 0;width:170px}
.hex{display:block;margin:0 auto}
.dots{font-size:16px;letter-spacing:3px;color:var(--brown);top:190px}
.btn{display:block;width:126px;height:38px;border-radius:20px;background:var(--amber);color:#fff;font-size:12px;font-weight:600;text-align:center;line-height:38px;box-shadow:0 3px 0 var(--amber-dark)}

/* store */
.store{left:0;top:1093px;width:1200px;height:613px;background:var(--paper)}
.card{background:#fff;border:2px solid var(--yellow-deep);border-radius:6px}
.product{top:135px;width:236px;height:347px;text-align:center}
.product .ph{position:absolute;left:48px;top:84px;width:140px;height:126px;border-radius:6px}
.stars{color:var(--star);font-size:9px;letter-spacing:1px}
.product .stars{position:absolute;left:0;width:100%;top:240px}
.product h4{position:absolute;left:0;width:100%;top:258px;font-family:"Raleway",sans-serif;font-weight:700;font-size:13px}
.product p{position:absolute;left:0;width:100%;top:282px;font-size:9px;color:var(--muted)}
.product .price{position:absolute;left:0;width:100%;top:304px;font-size:11px;font-weight:700;color:var(--orange)}
.price s{color:#bdb3a5;font-weight:500;margin-right:8px}

/* testimonials */
.testimonials{left:0;top:1706px;width:1200px;height:520px;background:
  radial-gradient(ellipse 380px 240px at 180px 180px,#ffe680 0%,transparent 70%),
  radial-gradient(ellipse 300px 200px at 1000px 300px,#f2c41a 0%,transparent 70%),
  var(--yellow)}
.quote{top:133px;width:233px;height:284px;border:none;border-radius:6px;padding:26px 24px 0}
.quote .who{display:flex;gap:12px;align-items:flex-start}
.avatar{width:28px;height:28px;border-radius:50%;background:linear-gradient(135deg,#d8b89a,#6b4a33);flex:none;margin-top:6px}
.who .stars{font-size:8px}
.who h5{font-family:"Signika",sans-serif;font-weight:600;font-size:15px;color:var(--brown)}
.who .role{font-size:9px;color:var(--orange)}
.quote blockquote{font-size:9.5px;font-style:italic;line-height:1.65;color:var(--muted);text-align:center;margin-top:16px}
.quote .mark{position:absolute;left:0;width:100%;bottom:8px;text-align:center;font-family:"Playfair Display",serif;font-size:46px;color:var(--star);line-height:1;height:30px}
.pager{left:560px;top:447px;display:flex;gap:17px}
.pager i{width:6px;height:6px;border-radius:50%;background:var(--brown);display:block}
.pager i.on{background:var(--orange)}

/* footer band */
.band{left:0;top:2226px;width:1200px;height:92px;background:var(--brown-band)}
.band .brand{left:240px;top:34px;color:var(--star);display:flex;gap:8px;align-items:center;font-size:20px;width:auto}
.band .brand .sq{margin:0}
.subscribe{left:480px;top:31px;width:256px;height:34px;background:#fff;border-radius:17px;border:3px solid var(--star)}
.subscribe span{position:absolute;left:16px;top:9px;font-size:9px;color:#9a8e7c}
.subscribe b{position:absolute;right:0;top:0;width:80px;height:28px;border-radius:14px;background:var(--star);font-size:8.5px;color:var(--brown);text-align:center;line-height:28px;font-weight:700}
.follow{left:789px;top:42px;font-size:11px;color:#fff;font-weight:600}
.social{left:857px;top:36px;display:flex;gap:7px}
.social i{width:22px;height:22px;border-radius:50%;background:var(--star);display:block}

/* footer */
.foot-col h6{font-family:"Signika",sans-serif;font-weight:600;font-size:14px;color:var(--orange);margin-bottom:22px}
.foot-col{top:2352px;font-size:9.5px;color:var(--brown)}
.about p{line-height:1.6;width:170px}
.about p b{color:var(--orange);font-weight:500}
.about ul{list-style:none;margin-top:22px}
.about li{display:flex;gap:10px;align-items:center;margin-bottom:10px}
.explore ul{list-style:none;display:grid;grid-template-columns:80px 80px;row-gap:14px}
.explore li::before{content:"›";color:var(--orange);margin-right:7px;font-weight:700}
.pill{display:inline-block;margin-top:18px;width:80px;height:20px;border-radius:10px;background:var(--orange);color:#fff;font-size:8px;text-align:center;line-height:20px}
.news .item{display:flex;gap:12px;margin-bottom:18px}
.news .thumb{width:68px;height:48px;border-radius:2px;background:linear-gradient(135deg,#f3b31a,#a86509)}
.news .date{font-size:8px;color:#9a8e7c}
.news .date::before{content:"";display:inline-block;width:6px;height:6px;background:var(--star);border-radius:1px;margin-right:5px}
.news .title{font-size:9.5px;font-weight:600;line-height:1.45;margin-top:4px;width:130px}

.bottombar{left:0;top:2576px;width:1200px;height:46px;background:var(--paper);font-size:9px;color:var(--brown)}
.bottombar .copy{left:234px;top:17px}
.to-top{left:947px;top:10px;width:26px;height:26px;border-radius:50%;background:var(--orange)}
</style>
</head>
<body>

<!-- top bar -->
<div class="abs topbar">
  <div class="abs contact">
    <span><svg width="10" height="10" viewBox="0 0 24 24"><path fill="#3b2106" d="M6.6 10.8a15 15 0 0 0 6.6 6.6l2.2-2.2c.3-.3.7-.4 1-.2 1.1.4 2.3.6 3.6.6.6 0 1 .4 1 1V20c0 .6-.4 1-1 1A17 17 0 0 1 3 4c0-.6.4-1 1-1h3.5c.6 0 1 .4 1 1 0 1.3.2 2.5.6 3.6.1.3 0 .7-.2 1z"/></svg>Phone +1 555 014 7730</span>
    <span><svg width="11" height="9" viewBox="0 0 24 18"><path fill="#3b2106" d="M0 0h24v18H0z"/><path fill="none" stroke="#fde9b2" stroke-width="2" d="M1 1l11 9 11-9"/></svg>info@ridgecrestapiary.com</span>
  </div>
  <div class="abs tools">
    <svg width="16" height="16" viewBox="0 0 24 24"><circle cx="10" cy="10" r="6.5" fill="none" stroke="#3b2106" stroke-width="3"/><path d="M15 15l6 6" stroke="#3b2106" stroke-width="3"/></svg>
    <svg width="17" height="17" viewBox="0 0 24 24"><circle cx="12" cy="12" r="10" fill="none" stroke="#3b2106" stroke-width="2.2"/><circle cx="12" cy="10" r="3.5" fill="#3b2106"/><path d="M6 18.5c1.5-2.5 3.5-3.5 6-3.5s4.5 1 6 3.5" fill="#3b2106"/></svg>
    <span style="position:relative"><svg width="18" height="16" viewBox="0 0 24 20"><path d="M1 6h22l-3 13H4z" fill="#3b2106"/><path d="M6 6l4-5M18 6l-4-5" stroke="#3b2106" stroke-width="2"/></svg><span class="cart-count">0</span></span>
  </div>
</div>

<!-- hero -->
<div class="abs hero" role="img" aria-label="Close-up photograph of honey bees crawling over a wooden hive frame"></div>
<div class="abs navband"></div>
<div class="abs brand"><span class="sq"></span>Ridgecrest<br>Apiary LLC</div>
<nav class="abs nav">
  <span>Home</span><span class="sep">-</span><span>About</span><span class="sep">-</span><span>Shop</span><span class="sep">-</span><span>Blog</span><span class="sep">-</span><span>Contact</span>
</nav>
<div class="abs badge">
  <svg width="312" height="356" viewBox="0 0 312 356">
    <polygon points="156,4 306,90 306,266 156,352 6,266 6,90" fill="none" stroke="#f3b51e" stroke-width="6"/>
    <polygon points="156,18 294,98 294,258 156,338 18,258 18,98" fill="rgba(25,18,10,.85)"/>
  </svg>
  <div class="text">
    <div class="kicker">Ridgecrest Apiary Provide</div>
    <h1>2019 NUCS &amp;<br>2019 QUEENS</h1>
    <span class="shop">SHOP NOW</span>
  </div>
</div>

<!-- services -->
<section class="abs services">
  <div class="abs svc-head center">
    <div class="eyebrow">What we do</div>
    <h2 class="sec-title">Our services</h2>
    <svg class="squiggle" width="34" height="6" viewBox="0 0 34 6"><path d="M1 3q4-4 8 0t8 0 8 0 8 0" fill="none" stroke="#ef6d2e" stroke-width="1.5"/></svg>
  </div>
  <p class="abs svc-intro center">Praesent id odio quis massa aliquet dictum ut eget erat. Aliquam erat volutpat. Pellentesque sit amet congue tellus.</p>

  <div class="abs svc-item" style="left:229px;top:141px">
    <svg class="hex" width="124" height="134" viewBox="0 0 124 134"><polygon points="62,3 121,36 121,98 62,131 3,98 3,36" fill="#fff" stroke="#fde9a0" stroke-width="4"/><circle cx="62" cy="67" r="30" fill="#fdf1ea" role="img" aria-label="Honeycomb icon"/></svg>
    <h3>Beekeeping Tips</h3>
    <p>Suspendisse mattis enim velit. Maecenas egestas mi auctor tortor imperdiet.</p>
  </div>
  <div class="abs svc-item" style="left:415px;top:141px">
    <svg class="hex" width="124" height="134" viewBox="0 0 124 134"><polygon points="62,3 121,36 121,98 62,131 3,98 3,36" fill="#fff" stroke="#fde9a0" stroke-width="4"/><circle cx="62" cy="67" r="30" fill="#fdf1ea" role="img" aria-label="Queen bee icon"/></svg>
    <h3>2019 Queen</h3>
    <p>Suspendisse mattis enim velit. Maecenas egestas mi auctor tortor imperdiet.</p>
  </div>
  <div class="abs svc-item" style="left:600px;top:141px">
    <svg class="hex" width="124" height="134" viewBox="0 0 124 134"><polygon points="62,3 121,36 121,98 62,131 3,98 3,36" fill="#fff" stroke="#fde9a0" stroke-width="4"/><circle cx="62" cy="67" r="30" fill="#fdf1ea" role="img" aria-label="Honey jar icon"/></svg>
    <h3>2019 Nucs</h3>
    <p>Suspendisse mattis enim velit. Maecenas egestas mi auctor tortor imperdiet.</p>
  </div>
  <div class="abs svc-item" style="left:785px;top:141px">
    <svg class="hex" width="124" height="134" viewBox="0 0 124 134"><polygon points="62,3 121,36 121,98 62,131 3,98 3,36" fill="#fff" stroke="#fde9a0" stroke-width="4"/><circle cx="62" cy="67" r="30" fill="#fdf1ea" role="img" aria-label="Beehive icon"/></svg>
    <h3>Swarm Remoal</h3>
    <p>Suspendisse mattis enim velit. Maecenas egestas mi auctor tortor imperdiet.</p>
  </div>
  <span class="abs dots" style="left:393px">.....</span>
  <span class="abs dots" style="left:579px">.....</span>
  <span class="abs dots" style="left:764px">.....</span>
  <span class="abs btn" style="left:534px;top:408px">Shop Now</span>
</section>

<!-- store -->
<section class="abs store">
  <div class="abs center" style="left:0;top:60px;width:1200px">
    <div class="eyebrow">Products</div>
    <h2 class="sec-title">Online store</h2>
    <svg class="squiggle" width="34" height="6" viewBox="0 0 34 6"><path d="M1 3q4-4 8 0t8 0 8 0 8 0" fill="none" stroke="#ef6d2e" stroke-width="1.5"/></svg>
  </div>
  <div class="abs" style="left:1040px;top:92px;width:160px;height:130px;border-radius:50% 0 0 50%;background:radial-gradient(circle at 60% 50%,#ffffff 0%,#f2ede6 60%,transparent 75%)" role="img" aria-label="White orchid sprig with a bee"></div>
  <div class="abs" style="left:0;top:428px;width:210px;height:178px;background:radial-gradient(circle at 30% 55%,#f3c9d4 0%,#f7e3e6 45%,transparent 72%)" role="img" aria-label="Pink magnolia blossoms with a bee"></div>

  <div class="abs card product" style="left:228px">
    <div class="ph" style="background:linear-gradient(90deg,#fff,#f4c07a 40%,#b86a1e 70%,#fff)" role="img" aria-label="Queen honey bee"></div>
    <div class="stars">★★★★★</div><h4>2019 Queen</h4>
    <p>Duis et aliquam orci. Vivamus augue quam ...</p>
    <div class="price"><s>$4.90</s>$1.99</div>
  </div>
  <div class="abs card product" style="left:476px">
    <div class="ph" style="background:linear-gradient(135deg,#e9a91a,#b5700d 55%,#6a3a08)" role="img" aria-label="Bees on golden honeycomb"></div>
    <div class="stars">★★★★★</div><h4>2019 Queen</h4>
    <p>Duis et aliquam orci. Vivamus augue quam ...</p>
    <div class="price"><s>$5.90</s>$1.99</div>
  </div>
  <div class="abs card product" style="left:724px">
    <div class="ph" style="background:linear-gradient(135deg,#6b5134,#3a2812 55%,#5c4428)" role="img" aria-label="Dense cluster of bees on a frame"></div>
    <div class="stars">★★★★★</div><h4>2019 Nucs</h4>
    <p>Duis et aliquam orci. Vivamus augue quam ...</p>
    <div class="price"><s>$4.90</s>$1.99</div>
  </div>
  <span class="abs btn" style="left:536px;top:524px">Shop Now</span>
</section>

<!-- testimonials -->
<section class="abs testimonials" role="img" aria-label="Soft yellow honeycomb and bee backdrop">
  <div class="abs center" style="left:0;top:40px;width:1200px">
    <div class="eyebrow">Testimonials</div>
    <h2 class="sec-title">What our clients say</h2>
    <svg class="squiggle" width="34" height="6" viewBox="0 0 34 6"><path d="M1 3q4-4 8 0t8 0 8 0 8 0" fill="none" stroke="#ef6d2e" stroke-width="1.5"/></svg>
  </div>

  <div class="abs card quote" style="left:233px">
    <div class="who"><span class="avatar"></span><div><div class="stars">★★★★★</div><h5>Marlene Quill</h5><div class="role">Top Manager</div></div></div>
    <blockquote>Lorem ipsum dolor sit amet, consectetur adipiscing elit. Nullam facilisis at turpis eu faucibus. In dignissim, enim eu ornare aliquet, metus ex tempor neque, sit amet efficitur turpis lorem et odio. Nam congue in orci at facilisis. In efficitur, leo non commodo lacinia, odio metus sodales purus, sed consequat lectus mi in purus.</blockquote>
    <div class="mark">”</div>
  </div>
  <div class="abs card quote" style="left:485px">
    <div class="who"><span class="avatar"></span><div><div class="stars">★★★★★</div><h5>Dorian Felt</h5><div class="role">Truck Driver</div></div></div>
    <blockquote>Duis et tellus imperdiet, lacinia risus id, tincidunt ipsum. Integer euismod elit vel nibh commodo, at consequat nisl rhoncus. Aliquam tempor lorem odio, non aliquam nunc egestas in. Proin rutrum justo ac lorem pellentesque pretium.</blockquote>
    <div class="mark">”</div>
  </div>
  <div class="abs card quote" style="left:737px">
    <div class="who"><span class="avatar"></span><div><div class="stars">★★★★★</div><h5>Lucia Brennard</h5><div class="role">Administrator</div></div></div>
    <blockquote>Nullam orci dui, dictum et magna sollicitudin, tempor blandit erat. Maecenas suscipit tellus sit amet augue placerat fringilla a id lacus. Fusce tincidunt in leo lacinia condimentum. Maecenas suscipit tellus sit amet augue placerat fringilla a id lacus. Fusce tincidunt in leo lacinia condimentum.</blockquote>
    <div class="mark">”</div>
  </div>
  <div class="abs pager"><i></i><i class="on"></i><i></i><i></i></div>
</section>

<!-- footer band -->
<div class="abs band">
  <div class="abs brand"><span class="sq"></span>Ridgecrest Apiary LLC</div>
  <div class="abs subscribe"><span>Type your email id</span><b>SUBSCRIBE</b></div>
  <div class="abs follow">Follow Us</div>
  <div class="abs social"><i></i><i></i><i></i><i></i></div>
</div>

<!-- footer -->
<div class="abs foot-col about" style="left:241px">
  <h6>About us</h6>
  <p><b>Address:</b> 48 Clover Lane, Ridgecrest, Valley County 8821-74</p>
  <ul>
    <li><svg width="10" height="10" viewBox="0 0 24 24"><path fill="#ef6d2e" d="M6.6 10.8a15 15 0 0 0 6.6 6.6l2.2-2.2c.3-.3.7-.4 1-.2 1.1.4 2.3.6 3.6.6.6 0 1 .4 1 1V20c0 .6-.4 1-1 1A17 17 0 0 1 3 4c0-.6.4-1 1-1h3.5c.6 0 1 .4 1 1 0 1.3.2 2.5.6 3.6.1.3 0 .7-.2 1z"/></svg>+1 555 014 2290</li>
    <li><svg width="10" height="8" viewBox="0 0 24 18"><path fill="#ef6d2e" d="M0 0h24v18H0z"/><path fill="none" stroke="#fff" stroke-width="2" d="M1 1l11 9 11-9"/></svg>orders@ridgecrestapiary.com</li>
    <li><svg width="10" height="10" viewBox="0 0 24 24"><circle cx="12" cy="12" r="10" fill="#ef6d2e"/></svg>ridgecrestapiary</li>
  </ul>
</div>
<div class="abs foot-col explore" style="left:487px">
  <h6>Explore</h6>
  <ul><li>Home</li><li>Gallery</li><li>About us</li><li>Contacts</li><li>Products</li><li>Pages</li><li>Blog</li></ul>
  <span class="pill">Contact us</span>
</div>
<div class="abs foot-col news" style="left:731px">
  <h6>Recent news</h6>
  <div class="item"><div class="thumb" role="img" aria-label="Bee on a yellow flower"></div><div><div class="date">May 12, 2018</div><div class="title">This season, increased yield of honey</div></div></div>
  <div class="item"><div class="thumb" role="img" aria-label="Beekeeper tending a hive"></div><div><div class="date">February 20, 2018</div><div class="title">Our beekeepers begin to collect honey</div></div></div>
</div>

<div class="abs bottombar">
  <div class="abs copy">© All Rights Reserved - 2019</div>
  <div class="abs to-top"><svg width="26" height="26" viewBox="0 0 26 26"><path d="M9 15l4-4 4 4" fill="none" stroke="#fff" stroke-width="2"/></svg></div>
</div>

</body>
</html>
```